Business Card Design Project - KLB

I am looking for a more sophisticated card design for my company,
"The Kestrel Bureau"

We are a consultancy focused on strategy and change in Associations and professional organisations.

I am a lawyer and psychologist with a PhD and so am looking for something that communicates seriousness and credibility but also quirky creative solutions for strategic problems, which is my field of speciality.

I am looking for something that is quietly spoken, rather than loud colours ('credible' and 'creative' are the two adjectives that I think of as competing here).

I particularly like an embossed card style - heavy white card with plain white or white and black or white and grey text.

The key logo image for the company is a question mark and I am open to suggestions and ideas on design.

I have attached a file that includes a couple of styles that have caught my eye and my thoughts on them. Hopefully they communicate what I'm looking for.
Updates

Thank you for all the great suggestions and designs.

I really appreciated the effort and creative energy you put into your designs. I have now closed the project after selecting a design and advising the successful designer of the card that I am happy with.

Regards

Target Market(s)

Organisations (CEO's and Boards), Governments, Legal professionals, Membership Associations and aspiring professionals.

Industry/Entity Type

Lawyer

Requirements
Must have
• The key logo element is a question mark (?) and this needs to be incorporated.

Embossed style - cut outs or other design ideas interest me too.

The attached file has a number of sample ideas and comments on each one that I like.
Should not have
• I like crisp, modern fonts (Myriads etc...) and do not like embellished fonts or Times etc...

```html
<!DOCTYPE html>
<html lang="en">
<head>
<meta charset="utf-8">
<title>The Kestrel Bureau – Business Card</title>
<link rel="stylesheet" href="https://fonts.googleapis.com/css2?family=Open+Sans:wght@400;700&display=swap">
<style>
  :root {
    --card-light: #dcdcdc;
    --card-dark: #2e2e2e;
    --text-heading: #555555;
    --text-body: #444444;
    --text-detail: #4a4a4a;
    --brand-text: #9a9a9a;
    --brand-ring: #7a7a7a;
  }
  html, body {
    margin: 0;
    padding: 0;
    width: 1200px;
    height: 720px;
    overflow: hidden;
    background: #ffffff;
  }
  .card {
    position: relative;
    width: 1200px;
    height: 720px;
    font-family: "Open Sans", Verdana, sans-serif;
    overflow: hidden;
  }
  .contact-side {
    position: absolute;
    left: 0;
    top: 0;
    width: 696px;
    height: 720px;
    background: var(--card-light);
  }
  .person {
    position: absolute;
    left: 28px;
    top: 206px;
    margin: 0;
    font-weight: 700;
    font-size: 33px;
    line-height: 42px;
    color: var(--text-heading);
  }
  .company {
    position: absolute;
    left: 28px;
    top: 346px;
    margin: 0;
    font-size: 29px;
    color: var(--text-body);
  }
  .details {
    position: absolute;
    left: 28px;
    top: 418px;
    margin: 0;
    padding: 0;
    list-style: none;
    font-size: 25px;
    color: var(--text-detail);
    white-space: nowrap;
  }
  .details li { height: 49px; line-height: 49px; }
  .brand-side {
    position: absolute;
    left: 696px;
    top: 0;
    width: 504px;
    height: 720px;
    background: var(--card-dark);
  }
  .brand-word {
    position: absolute;
    left: 0;
    width: 504px;
    text-align: center;
    margin: 0;
    font-size: 60px;
    line-height: 80px;
    font-weight: 400;
    color: var(--brand-text);
  }
  .brand-word.top { top: 28px; }
  .brand-word.bottom { top: 568px; }
  .brand-ring {
    position: absolute;
    left: 59px;
    top: 158px;
  }
</style>
</head>
<body>
  <div class="card">
    <section class="contact-side">
      <h1 class="person">Dr. Mara Ellison<br>Director</h1>
      <p class="company">The Kestrel Bureau</p>
      <ul class="details">
        <li>M::: +61400123456</li>
        <li>P::: +61290001234</li>
        <li>E::: mara@kestrelbureau.com.au</li>
        <li>PO::: P.O. Box 4410, Ashgrove Bay, Sydney, Australia</li>
      </ul>
    </section>
    <section class="brand-side">
      <p class="brand-word top">Kestrel</p>
      <svg class="brand-ring" width="386" height="386" viewBox="0 0 386 386" aria-hidden="true">
        <circle cx="193" cy="193" r="184" fill="none" stroke="var(--brand-ring)" stroke-width="17"/>
      </svg>
      <p class="brand-word bottom">Bureau</p>
    </section>
  </div>
</body>
</html>
```